Exciting Personal Development Book Cover: FIND ZEN NOW!

Design a Book Cover for my personal development book.
Title: Find Zen Now!
Author: Marcus Telly
Tagline: A real-life solution to get unstuck and break free

My picture must make up the front cover as I need to build my brand and people should recognise me on book shelves. Bold and catchy. How you do it is up to you. There must be space for a short testimonial from a famous person who is currently reading my book. I uploaded a sample of what I made in Photoshop but I don't have design skills.

I've added a PDF of my book so you can read the chapter index and introduction to get a sense of the content.

Target Market(s)

Personal Development Self-Help Market

Industry/Entity Type

Personal Development

Font styles to use
Serif
Sans Serif

Requirements
Must have
• My picture as hero image on cover.
Nice to have
• Must have Title, Tagline and my author name. If possible ZEN stands for 'Zeal, Energy & Nerve' If there is a way to fit this somewhere great. If it's too much then it can go somewhere on the back.

```html
<!DOCTYPE html>
<html lang="en">
<head>
<meta charset="utf-8">
<title>Find Zen Now! — Marcus Telly</title>
<link rel="stylesheet" href="https://fonts.googleapis.com/css2?family=Anton&family=Montserrat:wght@500;600;700;900&display=swap">
<style>
  :root {
    --cover-blue: #1670c4;
    --cover-blue-deep: #0f5ea9;
    --accent-blue: #1b9be6;
    --curl-light: #5aa9ea;
    --curl-mid: #2e8fe0;
    --ink: #000000;
    --white: #ffffff;
    --skin: #c69a80;
    --shirt: #eeeeee;
  }
  * { margin: 0; padding: 0; box-sizing: border-box; }
  html, body {
    width: 776px; height: 1200px; overflow: hidden;
    background: var(--cover-blue);
  }
  .cover {
    position: relative; width: 776px; height: 1200px; overflow: hidden;
    background: radial-gradient(ellipse at 60% 40%, var(--cover-blue) 0%, var(--cover-blue-deep) 100%);
    font-family: "Montserrat", Arial, sans-serif;
  }
  .cover-shapes, .author-photo { position: absolute; left: 0; top: 0; }

  .cover-title { font-size: inherit; }
  .title-word {
    position: absolute; font-weight: 900; line-height: 1; white-space: nowrap;
    transform-origin: center center;
  }
  .title-find {
    color: var(--white); font-size: 120px;
    left: 225px; top: 185px;
    transform: translate(-50%, -50%) rotate(-25deg);
  }
  .title-zen {
    color: var(--accent-blue); font-size: 155px;
    left: 397px; top: 318px;
    transform: translate(-50%, -50%) rotate(-25deg);
  }
  .title-now {
    color: var(--white); font-size: 110px;
    left: 365px; top: 582px;
    transform: translate(-50%, -50%) rotate(-28deg);
  }
  .zen-meaning {
    position: absolute; left: 445px; top: 384px;
    transform: translate(-50%, -50%) rotate(-29deg);
    color: var(--accent-blue); font-weight: 600; font-size: 20px;
    letter-spacing: 2.5px; text-transform: uppercase; white-space: nowrap;
  }

  .author-name {
    position: absolute; left: 250px; top: 905px;
    transform: translate(-50%, -50%) rotate(61.5deg);
    font-family: "Anton", Impact, sans-serif; font-size: 66px;
    color: var(--white); text-transform: uppercase; white-space: nowrap;
    letter-spacing: 1px;
  }

  .testimonial {
    position: absolute; left: 46px; width: 142px; top: 822px;
    text-align: center; color: var(--white);
  }
  .testimonial-mark {
    display: block; text-align: left; padding-left: 12px;
    font-weight: 900; font-size: 96px; line-height: 0.9; height: 58px;
    color: var(--accent-blue);
  }
  .testimonial-quote {
    margin-top: 44px;
    font-weight: 500; font-size: 16px; line-height: 21.6px;
  }
  .testimonial-name {
    margin-top: 26px; margin-left: -20px; margin-right: -20px;
    font-weight: 700; font-size: 17px; color: var(--accent-blue);
  }
</style>
</head>
<body>
<main class="cover">
  <svg class="cover-shapes" width="776" height="1200" viewBox="0 0 776 1200" aria-hidden="true">
    <defs>
      <linearGradient id="curl-shade" x1="0" y1="0" x2="1" y2="0">
        <stop offset="0" stop-color="var(--curl-mid)"/>
        <stop offset="0.55" stop-color="var(--curl-light)"/>
        <stop offset="1" stop-color="var(--curl-mid)"/>
      </linearGradient>
    </defs>
    <polygon class="lower-band" points="0,534 353,1200 0,1200" fill="var(--ink)"/>
    <polygon class="torn-window" fill="var(--ink)"
      points="112,349 160,322 205,302 260,262 320,236 380,198 440,172 500,135 560,110 634,60 650,98 668,132 690,178 712,220 733,259 690,280 640,305 580,330 520,362 460,390 400,420 340,452 280,488 233,517 205,470 175,425 140,385"/>
    <polygon class="paper-curl" fill="url(#curl-shade)"
      points="0,440 112,349 140,385 175,425 205,470 233,517 252,560 250,640 200,670 165,672 0,540"/>
  </svg>

  <h1 class="cover-title">
    <span class="title-word title-find">FIND</span>
    <span class="title-word title-zen">ZEN</span>
    <span class="title-word title-now">NOW!</span>
  </h1>
  <p class="zen-meaning">Zeal, Energy &amp; Nerve</p>

  <svg class="author-photo" width="776" height="1200" viewBox="0 0 776 1200" role="img" aria-label="Cut-out portrait of author Marcus Telly smiling in a white shirt, arms crossed">
    <defs>
      <linearGradient id="photo-tones" x1="0" y1="0" x2="0" y2="1">
        <stop offset="0" stop-color="#3a2c25"/>
        <stop offset="0.1" stop-color="var(--skin)"/>
        <stop offset="0.33" stop-color="var(--skin)"/>
        <stop offset="0.42" stop-color="var(--shirt)"/>
        <stop offset="0.8" stop-color="#e2e2e2"/>
        <stop offset="0.9" stop-color="#b9785a"/>
        <stop offset="1" stop-color="#f0f0f0"/>
      </linearGradient>
    </defs>
    <path fill="url(#photo-tones)"
      d="M560,470 C556,385 630,348 680,349 C740,352 762,400 755,470 L760,560 L776,590 L776,1200 L400,1200 L388,1000 L395,760 C410,700 470,655 560,640 Z"/>
  </svg>

  <p class="author-name">Marcus Telly</p>

  <blockquote class="testimonial">
    <span class="testimonial-mark">”</span>
    <p class="testimonial-quote">Lorem ipsum dolor sit amet, consectetur adipiscing elit. Nulla aliquet, massa cursus consectetur lacinia,</p>
    <p class="testimonial-name">Name Surname</p>
  </blockquote>
</main>
</body>
</html>
```